Business Card Design Project

beauty / make up / lashes

Industry/Entity Type

Business

Contact Information for Business Card

pink / gold / wait / black vintage classic elegant design

```html
<!DOCTYPE html>
<html lang="en">
<head>
<meta charset="utf-8">
<title>Lume Lashes – Business Card</title>
<link rel="stylesheet" href="https://fonts.googleapis.com/css2?family=Lato:wght@400;700&display=swap">
<style>
  :root {
    --page: #e6e6e6;
    --card-white: #fafafa;
    --card-grey: #8c8c8c;
    --frame-white: #f7f7f7;
    --teal: #1b9c98;
    --ink: #2b2b2b;
    --ornament: #6e6e6e;
    --divider: #9a9a9a;
  }
  * { box-sizing: border-box; margin: 0; padding: 0; }
  html, body { width: 1200px; height: 873px; overflow: hidden; }
  body {
    background: var(--page);
    font-family: "Lato", sans-serif;
    position: relative;
  }
  .card {
    position: absolute;
    left: 285px;
    width: 630px;
    height: 360px;
    border-radius: 18px;
    box-shadow: 0 6px 18px rgba(0,0,0,0.18);
    overflow: hidden;
  }
  /* Back side */
  .card--back { top: 48px; background: var(--card-grey); }
  .back-frame {
    position: absolute;
    left: 90px; top: 60px;
    width: 450px; height: 240px;
    border-radius: 60px;
    background: radial-gradient(ellipse at center, var(--frame-white) 55%, #d4d4d4 100%);
  }
  .back-brand {
    position: absolute;
    left: 0; right: 0; top: 155px;
    text-align: center;
    color: var(--teal);
    font-weight: 700;
    font-size: 40px;
    letter-spacing: 1px;
  }
  /* Front side */
  .card--front { top: 465px; background: var(--card-white); }
  .corner-ornament {
    position: absolute;
    width: 92px; height: 80px;
    background: radial-gradient(ellipse at center, #8a8a8a 0%, #bdbdbd 70%, rgba(189,189,189,0) 100%);
    opacity: 0.8;
  }
  .corner-ornament--tl { left: 14px; top: 14px; }
  .corner-ornament--tr { right: 14px; top: 14px; }
  .corner-ornament--bl { left: 14px; bottom: 14px; }
  .corner-ornament--br { right: 14px; bottom: 14px; }
  .front-brand {
    position: absolute;
    left: 60px; top: 158px;
    width: 220px;
    text-align: center;
    color: var(--teal);
    font-weight: 700;
    font-size: 34px;
    letter-spacing: 0.5px;
  }
  .divider {
    position: absolute;
    left: 305px; top: 80px;
    width: 2px; height: 190px;
    background: linear-gradient(to bottom, rgba(154,154,154,0), var(--divider) 50%, rgba(154,154,154,0));
  }
  .contact {
    position: absolute;
    left: 335px; top: 108px;
  }
  .contact__name {
    color: var(--teal);
    font-weight: 700;
    font-size: 22px;
  }
  .contact__role {
    color: var(--ink);
    font-size: 14px;
    margin: 4px 0 0 12px;
  }
  .contact__list {
    list-style: none;
    margin: 22px 0 0 30px;
  }
  .contact__item {
    display: flex;
    align-items: center;
    gap: 12px;
    color: var(--ink);
    font-size: 15px;
    margin-bottom: 12px;
  }
  .contact__icon { width: 15px; height: 15px; fill: var(--teal); flex: none; }
</style>
</head>
<body>

  <section class="card card--back" aria-label="Business card, back">
    <div class="back-frame" role="img" aria-label="White scalloped frame with swirl ornaments"></div>
    <div class="back-brand">Lume Lashes</div>
  </section>

  <section class="card card--front" aria-label="Business card, front">
    <div class="corner-ornament corner-ornament--tl" role="img" aria-label="Filigree corner ornament"></div>
    <div class="corner-ornament corner-ornament--tr" role="img" aria-label="Filigree corner ornament"></div>
    <div class="corner-ornament corner-ornament--bl" role="img" aria-label="Filigree corner ornament"></div>
    <div class="corner-ornament corner-ornament--br" role="img" aria-label="Filigree corner ornament"></div>

    <div class="front-brand">Lume Lashes</div>
    <div class="divider"></div>

    <div class="contact">
      <p class="contact__name">Elena Marsh</p>
      <p class="contact__role">Owner / Founder</p>
      <ul class="contact__list">
        <li class="contact__item">
          <svg class="contact__icon" viewBox="0 0 24 24" aria-hidden="true"><path d="M6.6 10.8a15.1 15.1 0 0 0 6.6 6.6l2.2-2.2a1 1 0 0 1 1-.25 11.4 11.4 0 0 0 3.6.57 1 1 0 0 1 1 1V20a1 1 0 0 1-1 1A17 17 0 0 1 3 4a1 1 0 0 1 1-1h3.5a1 1 0 0 1 1 1c0 1.25.2 2.45.57 3.57a1 1 0 0 1-.25 1z"/></svg>
          1.555.013.0482
        </li>
        <li class="contact__item">
          <svg class="contact__icon" viewBox="0 0 24 24" aria-hidden="true"><path d="M2 5h20v14H2z M2 5l10 8 10-8" fill="var(--teal)"/><path d="M3 6l9 7 9-7" fill="none" stroke="#fafafa" stroke-width="1.6"/></svg>
          elena@lumelashstudio.com
        </li>
      </ul>
    </div>
  </section>

</body>
</html>
```